Brisk Bookings needs a New Home page

We provide online appointment scheduling. There are many schedulers out there. Ours is unique because the scheduler is shown in one compact view that can be easily incorporated into the customer's website or Chatterbay page. Whether our customer is a solo hair-stylist or a large testing center with hundreds of testing seats at multiple locations, our customer still gets the same easy-to-use, one-page scheduling experience.

Our current home page, briskbookings.example, feels cluttered and outdated. We want something more modern and minimal.

Here are web pages we like:
artmosaic.example
tillquay.example
ruvel.example

We are not unhappy with the current logo or color scheme.

Need very clear call(s) to action (i.e. sign up for trial, schedule a demo).
Design needs to look good on devices of varying size.

Here are some ideas:
“Simple Online Scheduling” - Simple, compact design, easy-to-use & powerful, time-saving, chaos-taming, affordable, one page scheduling
“Stay in touch” - Basic email confirmations, reminders or targeted email notifications for follow-ups, no shows and more
“Multiple locations? No problem” - Schedule for multiple locations on one scheduler -
“Resource Pools” - Batting cages, clerks at the DMV, computers in a lab, pilates reformer machines
“Go Social” - Scheduling for Chatterbay and mobile devices
“Visual Reporting” - Reports
“Trusted” - Testimonials, reliable since 2005, etc.
List of industries (with links to industry-specific pages)

Ultimately want to redevelop the full site.
Updates

Reason: Please do not submit any new designs. We are now just wrapping up polling and discussing details. Thank you to all designers who have submitted. We feel lucky to get to chose from many great designs.

Target Market(s)

Audience is very broad including solo entrepreneurs (massage therapist, accountants, lawyers), educational institutions (elementary schools, university departments, advisers, testing centers), health care providers and screening services, to government.

Industry/Entity Type

Online

Requirements
Must have
• Call(s) to action, i.e. sign up for trial, schedule a demo.
• Look good on devices of different sizes.

```html
<!DOCTYPE html>
<html lang="en">
<head>
<meta charset="utf-8">
<title>Brisk Bookings – Online Appointment Scheduling</title>
<link rel="stylesheet" href="https://fonts.googleapis.com/css2?family=Open+Sans:wght@300;400;600;700&display=swap">
<style>
:root{
  --blue:#1e90d8;
  --blue-light:#4db3ee;
  --blue-dark:#0f73c4;
  --nav-active:#5aaee8;
  --orange:#fbb829;
  --orange-edge:#f29a12;
  --text:#333;
  --muted:#666;
  --soft-bg:#f3f4f4;
  --line:#dcdcdc;
  --dark-band:#575757;
  --green:#2aa876;
}
*{box-sizing:border-box;margin:0;padding:0}
html,body{width:1200px;height:2829px;overflow:hidden}
body{font-family:"Open Sans",Arial,sans-serif;color:var(--text);background:#fff;position:relative}
.abs{position:absolute}

/* header */
.site-header{top:0;left:0;width:1200px;height:150px;background:#fff}
.brand{left:80px;top:60px;display:flex;align-items:center;gap:16px}
.brand-name{font-size:27px;font-weight:400;letter-spacing:.5px;color:#333;text-transform:uppercase}
.main-nav{right:80px;top:74px;display:flex;gap:6px}
.main-nav a{font-size:15px;color:#333;text-decoration:none;padding:9px 14px;text-transform:uppercase}
.main-nav a.active{background:var(--nav-active);color:#fff}

/* hero */
.hero{top:150px;left:0;width:1200px;height:485px;background:linear-gradient(120deg,#5fc2f4 0%,#2a9ae4 55%,#3aa9ec 100%)}
.hero-title{left:200px;top:145px;font-size:36px;font-weight:300;color:#fff;letter-spacing:1px}
.hero-list{left:200px;top:210px;list-style:none}
.hero-list li{color:#fff;font-size:17px;display:flex;align-items:center;gap:16px;height:44px}
.hero-arrow{top:190px;width:60px;height:60px;border-radius:50%;background:rgba(0,80,140,.35);display:flex;align-items:center;justify-content:center}
.hero-devices{left:620px;top:55px;width:360px;height:340px;border-radius:22px;background:linear-gradient(160deg,#3a3a3a,#111)}

/* welcome */
.welcome{top:635px;left:0;width:1200px;height:315px;background:var(--soft-bg);text-align:center}
.welcome h1{position:absolute;left:0;top:42px;width:100%;font-size:29px;font-weight:300;color:var(--blue)}
.welcome p{position:absolute;top:105px;left:115px;width:970px;font-size:13.5px;line-height:26px;color:var(--muted)}
.cta{position:absolute;top:188px;height:57px;width:214px;font-size:17px;line-height:51px;text-transform:uppercase;color:#fff;text-decoration:none}
.cta-trial{left:363px;background:var(--orange);border:3px solid var(--orange-edge)}
.cta-demo{left:617px;background:var(--blue-light);border:3px solid var(--blue-dark)}

/* features */
.features{top:950px;left:0;width:1200px;height:365px;background:#fff}
.feature{position:absolute;top:85px;width:260px;text-align:center}
.feature h3{margin-top:18px;font-size:22px;font-weight:400;color:var(--blue);text-transform:uppercase}
.feature p{margin-top:6px;font-size:14px;line-height:20px;color:var(--muted)}

/* scheduling */
.scheduling{top:1315px;left:0;width:1200px;height:375px;background:var(--soft-bg);overflow:hidden}
.scheduling h2{position:absolute;left:125px;top:42px;font-size:29px;font-weight:400;color:var(--blue)}
.scheduling p{position:absolute;left:125px;top:100px;width:500px;font-size:14px;line-height:25px;color:var(--muted)}
.checks{position:absolute;left:125px;top:222px;width:500px;display:grid;grid-template-columns:260px 240px;row-gap:20px;list-style:none}
.checks li{font-size:15px;color:var(--muted);display:flex;align-items:center;gap:14px}
.phone-frame{left:720px;top:30px;width:240px;height:380px;border-radius:36px;background:#fafafa;border:2px solid #d0d0d0}
.phone-screen{left:18px;top:68px;width:200px;height:260px;background:linear-gradient(160deg,#7b6bd8,#c98ed8 60%,#eef0f8)}

/* resources */
.resources{top:1690px;left:0;width:1200px;height:480px;background:#fff}
.resource-devices{left:135px;top:60px;width:345px;height:345px;border-radius:20px;background:linear-gradient(160deg,#2a2a2a,#0e0e0e)}
.connector{left:545px;width:200px;height:2px;background:var(--line)}
.connector::before{content:"";position:absolute;left:-4px;top:-4px;width:10px;height:10px;border-radius:50%;background:#b5b5b5}
.resource-icon{left:750px;width:80px;height:80px;border-radius:50%;border:2px solid var(--blue);display:flex;align-items:center;justify-content:center}
.resource-text{left:852px;width:260px}
.resource-text h4{font-size:21px;font-weight:400;color:var(--blue)}
.resource-text p{font-size:14px;line-height:22px;color:var(--muted);margin-top:6px}

/* testimonial */
.testimonial{top:2170px;left:0;width:1200px;height:300px;background:#fff;text-align:center}
.testimonial .rule{position:absolute;left:115px;top:45px;width:970px;height:2px;background:#e3e3e3}
.quote-badge{position:absolute;left:550px;top:0;width:100px;height:100px;border-radius:50%;background:#fff;border:2px solid #e3e3e3;font-size:70px;line-height:120px;color:#555;font-weight:700}
.testimonial h2{position:absolute;left:0;top:88px;width:100%;font-size:21px;font-weight:400;color:var(--blue)}
.testimonial blockquote{position:absolute;left:165px;top:130px;width:870px;font-size:13.5px;line-height:26px;color:var(--muted)}
.big-quote{position:absolute;font-size:60px;line-height:60px;color:#bbb;font-weight:700}
.testimonial cite{position:absolute;left:0;top:198px;width:100%;font-style:normal;font-size:16px;color:var(--blue)}
.testimonial cite span{font-size:13px}

/* clients */
.clients{top:2470px;left:0;width:1200px;height:230px;background:var(--dark-band);text-align:center}
.clients h2{position:absolute;left:0;top:45px;width:100%;font-size:21px;font-weight:400;color:#fff;text-transform:uppercase}
.client-row{position:absolute;top:115px;left:100px;width:1000px;display:flex;justify-content:space-between;align-items:center}
.client{display:flex;align-items:center;gap:12px;color:#fff;font-size:30px;font-weight:600}
.client .dot{width:34px;height:34px;border-radius:50%;background:#fff}

/* footer */
.site-footer{top:2700px;left:0;width:1200px;height:129px;background:#fff}
.footer-links{left:88px;top:40px;font-size:13px;color:#333}
.footer-links span{margin:0 10px;color:#999}
.copyright{left:88px;top:72px;font-size:13px;color:#333}
.social{left:880px;top:40px;display:flex;gap:20px}
.social a{width:36px;height:36px;display:block;text-decoration:none;color:#fff;font-size:11px;text-align:center;line-height:36px;font-weight:600}
</style>
</head>
<body>

<header class="site-header abs">
  <div class="brand abs">
    <svg width="56" height="50" viewBox="0 0 56 50" aria-hidden="true"><rect x="8" y="8" width="40" height="34" fill="#1e90d8"/></svg>
    <span class="brand-name">Brisk Bookings</span>
  </div>
  <nav class="main-nav abs">
    <a class="active" href="#">Home</a><a href="#">About</a><a href="#">Slotdeck</a><a href="#">Multiple Locations</a><a href="#">Contact</a>
  </nav>
</header>

<section class="hero abs">
  <div class="hero-arrow abs" style="left:80px"><svg width="16" height="24" viewBox="0 0 16 24"><path d="M12 3 L4 12 L12 21" stroke="#fff" stroke-width="3" fill="none"/></svg></div>
  <div class="hero-arrow abs" style="left:1050px"><svg width="16" height="24" viewBox="0 0 16 24"><path d="M4 3 L12 12 L4 21" stroke="#fff" stroke-width="3" fill="none"/></svg></div>
  <h2 class="hero-title abs">STAY IN TOUCH</h2>
  <ul class="hero-list abs">
    <li><svg width="22" height="22" viewBox="0 0 22 22"><circle cx="11" cy="11" r="9" stroke="#fff" stroke-width="2" fill="none"/><path d="M6 11 L10 15 L17 7" stroke="#fff" stroke-width="2.5" fill="none"/></svg>Basic email confirmations,</li>
    <li><svg width="22" height="22" viewBox="0 0 22 22"><circle cx="11" cy="11" r="9" stroke="#fff" stroke-width="2" fill="none"/><path d="M6 11 L10 15 L17 7" stroke="#fff" stroke-width="2.5" fill="none"/></svg>Reminders or targeted email notification</li>
    <li><svg width="22" height="22" viewBox="0 0 22 22"><circle cx="11" cy="11" r="9" stroke="#fff" stroke-width="2" fill="none"/><path d="M6 11 L10 15 L17 7" stroke="#fff" stroke-width="2.5" fill="none"/></svg>No shows and more</li>
  </ul>
  <div class="hero-devices abs" role="img" aria-label="Tablet and phone showing the Brisk Bookings scheduler"></div>
</section>

<section class="welcome abs">
  <h1>WELCOME TO OUR WEBSITE</h1>
  <p>Curabitur ut risus. Nullam suscipit enim vel rhoncus lobortis ipsum lorem condimentum nunc sit amet posuere nisi urna non libero. Donec blandit sem sit amet cursus fermentum neque risus gravida enim eget varius. Nullam suscipit enim vel rhoncus lobortis ipsum lorem</p>
  <a class="cta cta-trial" href="#">Sign up for trial</a>
  <a class="cta cta-demo" href="#">Schedule a demo</a>
</section>

<section class="features abs">
  <div class="feature" style="left:105px">
    <svg width="90" height="80" viewBox="0 0 90 80" aria-hidden="true">
      <path d="M45 44 L85 58 L45 72 L5 58 Z" fill="#e2474b"/>
      <path d="M45 30 L85 44 L45 58 L5 44 Z" fill="#2bb673"/>
      <path d="M45 16 L85 30 L45 44 L5 30 Z" fill="#6a8fd8"/>
    </svg>
    <h3>Simplify</h3>
    <p>Lorem ipsum dolor sit amet adipis mean. Morbi ut elit ultipum tristiquea Pellentesque habitant morbi.</p>
  </div>
  <div class="feature" style="left:470px">
    <svg width="90" height="80" viewBox="0 0 90 80" aria-hidden="true">
      <circle cx="45" cy="40" r="30" fill="none" stroke="#8a8a8a" stroke-width="14" stroke-dasharray="9 6"/>
      <circle cx="45" cy="40" r="24" fill="#9a9a9a"/>
      <circle cx="45" cy="40" r="11" fill="#fff"/>
    </svg>
    <h3>Save time</h3>
    <p>Lorem ipsum dolor sit amet adipis mean. Morbi ut elit ultipum tristiquea Pellentesque habitant morbi.</p>
  </div>
  <div class="feature" style="left:820px">
    <svg width="90" height="80" viewBox="0 0 90 80" aria-hidden="true">
      <circle cx="45" cy="40" r="38" fill="var(--green)"/>
      <path d="M28 40 L41 53 L63 28" stroke="#fff" stroke-width="8" fill="none"/>
    </svg>
    <h3>It' s affordable</h3>
    <p>Lorem ipsum dolor sit amet adipis mean. Morbi ut elit ultipum tristiquea Pellentesque habitant morbi.</p>
  </div>
</section>

<section class="scheduling abs">
  <h2>Simple Online Scheduling</h2>
  <p>Lorem Ipsum. Proin gravida nibh vel velit auctor aliquet. Aenean sollicitudin lorem quis bibendum auctor, nisi elit consequat ipsum, nec sagittis sem nibh id elit. Duis sed odio sit amet nibh vulputate cursus a sit amet mauris.</p>
  <ul class="checks">
    <li><svg width="16" height="16" viewBox="0 0 16 16"><rect x="1" y="1" width="14" height="14" fill="none" stroke="#999"/><path d="M4 8 L7 11 L13 4" stroke="#2a9ae4" stroke-width="2" fill="none"/></svg>Simple</li>
    <li><svg width="16" height="16" viewBox="0 0 16 16"><rect x="1" y="1" width="14" height="14" fill="none" stroke="#999"/><path d="M4 8 L7 11 L13 4" stroke="#2a9ae4" stroke-width="2" fill="none"/></svg>Time-saving</li>
    <li><svg width="16" height="16" viewBox="0 0 16 16"><rect x="1" y="1" width="14" height="14" fill="none" stroke="#999"/><path d="M4 8 L7 11 L13 4" stroke="#2a9ae4" stroke-width="2" fill="none"/></svg>Compact design</li>
    <li><svg width="16" height="16" viewBox="0 0 16 16"><rect x="1" y="1" width="14" height="14" fill="none" stroke="#999"/><path d="M4 8 L7 11 L13 4" stroke="#2a9ae4" stroke-width="2" fill="none"/></svg>Chaos-taming</li>
    <li><svg width="16" height="16" viewBox="0 0 16 16"><rect x="1" y="1" width="14" height="14" fill="none" stroke="#999"/><path d="M4 8 L7 11 L13 4" stroke="#2a9ae4" stroke-width="2" fill="none"/></svg>Easy-to-use &amp; powerful</li>
    <li><svg width="16" height="16" viewBox="0 0 16 16"><rect x="1" y="1" width="14" height="14" fill="none" stroke="#999"/><path d="M4 8 L7 11 L13 4" stroke="#2a9ae4" stroke-width="2" fill="none"/></svg>Affordable</li>
  </ul>
  <div class="phone-frame abs">
    <div class="phone-screen abs" role="img" aria-label="Phone screen showing a scheduling web page"></div>
  </div>
</section>

<section class="resources abs">
  <div class="resource-devices abs" role="img" aria-label="Tablet and phone showing the booking form on a mobile site"></div>

  <div class="connector abs" style="top:115px"></div>
  <div class="resource-icon abs" style="top:75px"><svg width="34" height="34" viewBox="0 0 34 34"><path d="M13 4 H21 M15 4 V14 L6 29 H28 L19 14 V4" stroke="#1e90d8" stroke-width="2.5" fill="none"/></svg></div>
  <div class="resource-text abs" style="top:72px"><h4>Resource Pools</h4><p>There are many variations of passages of Lorem Ipsum available, but thejest.</p></div>

  <div class="connector abs" style="top:230px"></div>
  <div class="resource-icon abs" style="top:190px"><svg width="34" height="34" viewBox="0 0 34 34"><rect x="10" y="3" width="14" height="28" rx="2" stroke="#1e90d8" stroke-width="2.5" fill="none"/><circle cx="17" cy="26" r="1.5" fill="#1e90d8"/></svg></div>
  <div class="resource-text abs" style="top:188px"><h4>Visual Reporting</h4><p>There are many variations of passages of Lorem Ipsum available, but thejest.</p></div>

  <div class="connector abs" style="top:355px"></div>
  <div class="resource-icon abs" style="top:315px"><svg width="34" height="34" viewBox="0 0 34 34"><path d="M17 31 C9 21 7 17 7 13 A10 10 0 0 1 27 13 C27 17 25 21 17 31 Z" stroke="#1e90d8" stroke-width="2.5" fill="none"/><circle cx="17" cy="13" r="3.5" fill="#1e90d8"/></svg></div>
  <div class="resource-text abs" style="top:313px"><h4>Multiple Locations</h4><p>There are many variations of passages of Lorem Ipsum available, but thejest.</p></div>
</section>

<section class="testimonial abs">
  <div class="rule"></div>
  <div class="quote-badge">&ldquo;</div>
  <h2>WHAT CLIENT SAYS?</h2>
  <span class="big-quote" style="left:132px;top:115px">&ldquo;</span>
  <blockquote>Lorem ipsum dolor sit amet, consectetur adipisicing elit. Et, modi libero possimus quos recusandae quibusdam adipisci autem fuga accusa nium iste nam culpa expedita nisi inventore tenetur ipsa eligendi architecto. Eveniet Lorem ipsum dolor sit amet, consectetur.</blockquote>
  <span class="big-quote" style="left:1030px;top:155px">&rdquo;</span>
  <cite>- Dana Merrow, <span>Manager at Halvern</span></cite>
</section>

<section class="clients abs">
  <h2>Clients we work with</h2>
  <div class="client-row">
    <span class="client">Orvo</span>
    <span class="client"><span class="dot"></span>Kelt</span>
    <span class="client">Tarnell</span>
    <span class="client"><span class="dot"></span>Lumo</span>
    <span class="client">Brightmere</span>
  </div>
</section>

<footer class="site-footer abs">
  <div class="footer-links abs">Terms and Conditions<span>|</span>Privacy Policy</div>
  <div class="copyright abs">Copyrights 2013. All Rights Reserved.</div>
  <div class="social abs">
    <a href="#" style="background:#3b5b9a" aria-label="Chatterbay">CB</a>
    <a href="#" style="background:#2aa4e0" aria-label="Chirpline">CL</a>
    <a href="#" style="background:#f2711c" aria-label="Feed">
      <svg width="36" height="36" viewBox="0 0 36 36"><circle cx="12" cy="24" r="2.5" fill="#fff"/><path d="M10 16 A10 10 0 0 1 20 26 M10 10 A16 16 0 0 1 26 26" stroke="#fff" stroke-width="2.5" fill="none"/></svg>
    </a>
    <a href="#" style="background:#d8352c" aria-label="Reelhub">RH</a>
  </div>
</footer>

</body>
</html>
```